BLAC inc Business Card Design

I have a rough draft of the BLAC inc logo that I would like to use on the business card. I also attached our logo for Quillbrook.com. I also included a sample of a business card from another mortgage company that I like. We would like a tagline on the back to say "let's get started" and below Quillbrook.com
Contact Information for Business Card
Brightway Lending and Capital, inc
Marcus Delane
Mortgage Specialist
Direct (555)204-1187
Cell (555)318-4592
Fax (555)907-2263
marcus@quillbrook.com
California Division of Parcel Registry 07493128
FLRB 460315

```html
<!DOCTYPE html>
<html lang="en">
<head>
<meta charset="utf-8">
<title>BLAC inc Business Card</title>
<link rel="stylesheet" href="https://fonts.googleapis.com/css2?family=Arimo:wght@400;700&family=Kaushan+Script&display=swap">
<style>
  :root {
    --bg: #ececec;
    --green: #7a9147;
    --navy: #1b2350;
    --white: #ffffff;
    --grey: #4a4a4a;
    --faint: #f1f1f1;
  }
  * { box-sizing: border-box; margin: 0; padding: 0; }
  html, body { width: 1200px; height: 821px; overflow: hidden; }
  body {
    background: var(--bg);
    font-family: "Arimo", Arial, sans-serif;
    display: flex;
    align-items: center;
    justify-content: center;
    gap: 48px;
  }
  .card {
    position: relative;
    width: 520px;
    height: 300px;
    overflow: hidden;
    box-shadow: 0 6px 18px rgba(0,0,0,.18);
  }

  /* Back side */
  .card-back {
    background: var(--green);
    color: var(--white);
  }
  .back-mark {
    position: absolute;
    left: 58px;
    top: 112px;
    width: 64px;
    height: 64px;
    border-radius: 50%;
    background: var(--white);
  }
  .tagline {
    position: absolute;
    left: 150px;
    top: 104px;
    font-family: "Kaushan Script", cursive;
    font-size: 48px;
    color: var(--navy);
    white-space: nowrap;
  }
  .back-url {
    position: absolute;
    right: 40px;
    top: 186px;
    font-size: 17px;
  }

  /* Front side */
  .card-front { background: var(--white); }
  .front-band {
    position: absolute;
    left: 0; right: 0; bottom: 0;
    height: 14px;
    background: var(--green);
  }
  .front-deco {
    position: absolute;
    left: -40px;
    bottom: -120px;
    width: 300px;
    height: 300px;
    border-radius: 50%;
    background: var(--faint);
  }
  .brand {
    position: absolute;
    left: 32px;
    top: 52px;
    display: flex;
    align-items: center;
    gap: 10px;
  }
  .brand-dot {
    width: 40px;
    height: 40px;
    border-radius: 50%;
    background: var(--navy);
  }
  .brand-name {
    font-size: 24px;
    font-weight: 700;
    color: var(--navy);
  }
  .person {
    position: absolute;
    left: 52px;
    top: 150px;
  }
  .person-name {
    font-size: 24px;
    color: var(--navy);
  }
  .person-role {
    font-size: 13px;
    color: var(--green);
    margin-top: 2px;
  }
  .contact {
    position: absolute;
    left: 262px;
    top: 34px;
    color: var(--navy);
  }
  .company {
    font-size: 26px;
    font-weight: 700;
    line-height: 1;
  }
  .company-full {
    font-size: 13px;
    color: var(--green);
    margin: 4px 0 14px;
  }
  .company-full b { color: var(--navy); font-weight: 400; }
  .line {
    font-size: 17px;
    font-weight: 700;
    line-height: 1.3;
    white-space: nowrap;
  }
  .line span {
    font-weight: 400;
    font-size: 14px;
    color: var(--grey);
  }
  .license {
    margin-top: 8px;
    font-size: 11px;
    line-height: 1.35;
    color: var(--grey);
  }
</style>
</head>
<body>
  <section class="card card-back">
    <div class="back-mark"></div>
    <p class="tagline">Let's get started!</p>
    <p class="back-url">Quillbrook.com</p>
  </section>

  <section class="card card-front">
    <div class="front-deco" role="img" aria-label="Faint decorative circle"></div>
    <div class="brand">
      <span class="brand-dot"></span>
      <span class="brand-name">Quillbrook.com</span>
    </div>
    <div class="person">
      <p class="person-name">Marcus Delane</p>
      <p class="person-role">Mortgage Specialist</p>
    </div>
    <div class="contact">
      <p class="company">BLAC inc</p>
      <p class="company-full"><b>B</b>rightway <b>L</b>ending <b>a</b>nd <b>C</b>apital, inc</p>
      <p class="line">(555)204-1187 <span>Direct</span></p>
      <p class="line">(555)318-4592 <span>Cell</span></p>
      <p class="line">(555)907-2263 <span>Fax</span></p>
      <p class="line">marcus@quillbrook.com</p>
      <p class="license">California Division of Parcel Registry<br>07493128<br>FLRB 460315</p>
    </div>
    <div class="front-band"></div>
  </section>
</body>
</html>
```